Business Card Design

We need a new business card design for a company based in Cedar Hollow, TX. We provide business consulting services in the information technology / services space. We like variations of the color blue, aqua, black, light tan, and white. Would like "cool" tones. The design should clearly communicate professionalism. Think outside the box - we don't want something "typical". Our company name is "Vantrell Advisory, LLC".
Updates

Thank you all for your submissions. We have seen some very creative and inspired designs. We have made a decision and will be moving forward with that design. Appreciate all of the hard work.

Industry/Entity Type

Information Technology

Contact Information for Business Card

Denise Harlow Trumbey
482 West Maple Ridge Dr.
Cedar Hollow, TX 76185

```html
<!DOCTYPE html>
<html lang="en">
<head>
<meta charset="utf-8">
<title>Vantrell Advisory, LLC — Business Card</title>
<link rel="stylesheet" href="https://fonts.googleapis.com/css2?family=Federo&display=swap">
<style>
  :root {
    --ink-black: #060807;
    --brand-aqua: #5fd6a8;
    --brand-blue: #3453e6;
    --accent-green: #7ee86c;
    --accent-tan: #eeee92;
    --streak-tan: rgba(238, 236, 160, 0.45);
    --skyline-shade: rgba(40, 46, 42, 0.3);
  }
  * { margin: 0; padding: 0; box-sizing: border-box; }
  html, body {
    width: 1200px;
    height: 702px;
    overflow: hidden;
    background: var(--ink-black);
  }
  .card {
    position: relative;
    width: 1200px;
    height: 702px;
    background: var(--ink-black);
    font-family: "Federo", sans-serif;
    text-transform: uppercase;
    overflow: hidden;
  }
  .skyline-art {
    position: absolute;
    left: 0;
    bottom: 0;
    width: 1200px;
    height: 300px;
    background: linear-gradient(to top, var(--skyline-shade), rgba(40, 46, 42, 0));
  }
  .light-streaks {
    position: absolute;
    right: 0;
    top: 0;
    width: 360px;
    height: 702px;
    background:
      radial-gradient(ellipse 240px 170px at 300px 250px, var(--streak-tan), rgba(238, 236, 160, 0) 75%),
      radial-gradient(ellipse 160px 240px at 330px 460px, rgba(200, 200, 140, 0.22), rgba(200, 200, 140, 0) 75%),
      radial-gradient(ellipse 130px 110px at 320px 40px, rgba(238, 236, 160, 0.35), rgba(238, 236, 160, 0) 75%);
  }
  .brand-name {
    position: absolute;
    left: 56px;
    top: 46px;
    color: var(--brand-aqua);
    font-size: 100px;
    line-height: 1;
    letter-spacing: 1px;
    white-space: nowrap;
    transform: scaleY(1.45);
    transform-origin: left top;
  }
  .brand-suffix {
    position: absolute;
    right: 620px;
    top: 194px;
    color: var(--brand-blue);
    font-size: 44px;
    line-height: 1;
    letter-spacing: 1px;
    white-space: nowrap;
    transform: scaleY(1.2);
    transform-origin: right top;
  }
  .contact-name {
    position: absolute;
    left: 0;
    width: 1200px;
    top: 358px;
    text-align: center;
    font-size: 44px;
    line-height: 1;
    letter-spacing: 2px;
    white-space: nowrap;
  }
  .name-first { color: var(--brand-blue); }
  .name-middle { color: var(--accent-green); }
  .name-last { color: var(--accent-tan); }
  .contact-phone {
    position: absolute;
    left: 0;
    width: 1200px;
    top: 428px;
    text-align: center;
    color: var(--accent-green);
    font-size: 24px;
    line-height: 1;
    letter-spacing: 1px;
  }
  .phone-icon {
    width: 18px;
    height: 26px;
    vertical-align: -5px;
    margin-right: 4px;
  }
  .contact-address {
    position: absolute;
    left: 0;
    width: 1200px;
    top: 614px;
    text-align: center;
    font-size: 34px;
    line-height: 1;
    letter-spacing: 2px;
    white-space: nowrap;
  }
  .street { color: var(--accent-tan); }
  .city { color: var(--accent-green); }
  .separator {
    display: inline-block;
    width: 12px;
    height: 8px;
    border-radius: 4px;
    border: 2px solid var(--accent-tan);
    margin: 0 12px;
    vertical-align: 4px;
  }
</style>
</head>
<body>
  <main class="card">
    <div class="skyline-art" role="img" aria-label="Faint city skyline silhouette in the background"></div>
    <div class="light-streaks" role="img" aria-label="Abstract sweeping pale tan light streaks"></div>

    <header class="brand">
      <span class="brand-name">Vantrell</span>
      <span class="brand-suffix">Advisory, LLC</span>
    </header>

    <p class="contact-name">
      <span class="name-first">Denise</span>
      <span class="name-middle">Harlow</span>
      <span class="name-last">Trumbey</span>
    </p>

    <p class="contact-phone">
      <svg class="phone-icon" viewBox="0 0 18 26" aria-hidden="true">
        <rect x="1" y="1" width="16" height="24" rx="1" fill="none" stroke="#7ee86c" stroke-width="2"/>
        <rect x="4" y="4" width="10" height="6" fill="none" stroke="#7ee86c" stroke-width="1.5"/>
        <g fill="#7ee86c">
          <rect x="4" y="13" width="2.5" height="2"/><rect x="8" y="13" width="2.5" height="2"/><rect x="12" y="13" width="2.5" height="2"/>
          <rect x="4" y="17" width="2.5" height="2"/><rect x="8" y="17" width="2.5" height="2"/><rect x="12" y="17" width="2.5" height="2"/>
          <rect x="4" y="21" width="2.5" height="2"/><rect x="8" y="21" width="2.5" height="2"/><rect x="12" y="21" width="2.5" height="2"/>
        </g>
      </svg>(817)-555-0143
    </p>

    <p class="contact-address">
      <span class="street">482 West Maple Ridge Dr.</span><span class="separator"></span><span class="city">Cedar Hollow, TX 76185</span>
    </p>
  </main>
</body>
</html>
```